Design for a Service-Based Estimate

We want a design for an Estimate that will always be sent in PDF format. The estimate or proposal is a critical document that needs to plainly show the service items, item description but also needs to be attractive and professional looking. Our current estimate deliverable is attached but it looks really basic like a Word document

```html
<!DOCTYPE html>
<html lang="en">
<head>
<meta charset="utf-8">
<title>Granite Lane – Estimate</title>
<link href="https://fonts.googleapis.com/css2?family=Open+Sans:wght@400;600;700;800&family=Arimo:wght@400&display=swap" rel="stylesheet">
<style>
  :root{
    --backdrop:#e4e9e9;
    --paper:#ffffff;
    --brand-red:#e8271f;
    --brand-dark:#0d111b;
    --brand-navy:#1d2a5c;
    --ink:#1a1a1a;
    --rule:#e2e2e2;
  }
  *{box-sizing:border-box;margin:0;padding:0}
  html,body{width:1200px;height:600px;overflow:hidden;background:var(--backdrop)}
  body{position:relative;font-family:"Open Sans",sans-serif;color:var(--ink)}
  .page{position:absolute;top:35px;width:377px;height:533px;background:var(--paper);box-shadow:0 4px 14px rgba(0,0,0,.18)}
  .page--estimate{left:109px}
  .page--terms{left:710px}
  .page-frame{position:absolute;inset:0}
  .brand-name{position:absolute;right:25px;top:27px;font-weight:800;font-size:19px;letter-spacing:1.5px;color:var(--brand-navy);line-height:1}
  .abs{position:absolute}
  .recipient{right:20px;top:137px;text-align:right;font-size:6.2px;line-height:9.5px}
  .rule{position:absolute;left:53px;width:304px;height:0;border-top:.6px solid var(--rule)}
  .project{left:53px;width:304px;text-align:center;font-size:6.2px}
  .project-title{top:185px;font-weight:600}
  .project-address{top:196px}
  .project-bid{top:210px}
  .line-items{position:absolute;left:53px;top:234px;width:304px;font-size:5.9px;border-collapse:collapse;letter-spacing:-.02px}
  .line-items th{font-weight:700;vertical-align:bottom;padding:0 4px 3px;line-height:8.5px}
  .line-items td{vertical-align:top;padding:4px 4px 5px;line-height:8.5px;border-top:.6px solid var(--rule)}
  .line-items .num{text-align:center}
  .line-items .money{text-align:right}
  .line-items .strong{font-weight:700}
  .line-items tr.total td{border-bottom:.6px solid var(--rule);padding-bottom:8px}
  .line-items th:first-child,.line-items td:first-child{text-align:left}
  .terms-box{position:absolute;left:56px;top:75px;width:306px;height:183px;border:.6px solid var(--rule)}
  .terms-title{height:19px;border-bottom:.6px solid var(--rule);text-align:center;font-size:7.4px;font-weight:600;line-height:18px}
  .terms-list{list-style:disc;padding:6px 6px 0 19px;font-size:5.3px;line-height:8.5px;letter-spacing:-.03px}
  .signature{position:absolute;left:252px;width:90px;border-top:.6px solid #333;font-size:6.2px;padding-top:3px}
  .contact{position:absolute;left:58px;font-family:"Arimo",sans-serif;font-size:6.4px;line-height:9px;color:#000}
  .contact-rule{position:absolute;left:24px;width:104px;border-top:.8px solid var(--brand-dark)}
</style>
</head>
<body>

<section class="page page--estimate">
  <svg class="page-frame" width="377" height="533" viewBox="0 0 377 533" aria-hidden="true">
    <polygon points="16,0 37,0 37,283 16,295" fill="var(--brand-red)"/>
    <polygon points="16,295 37,283 37,503 377,503 377,522 16,522" fill="var(--brand-dark)"/>
  </svg>
  <div class="brand-name">GRANITE LANE</div>

  <div class="abs recipient">
    To:<br>Dana Whitfield<br>48 Harbor Lane NE Tampa 33602<br>dwhitfield@mailbox.com
  </div>
  <div class="rule" style="top:179px"></div>
  <div class="abs project project-title">Dana Whitfield New Concrete Pad</div>
  <div class="abs project project-address">48 Harbor Lane NE Tampa 33602</div>
  <div class="abs project project-bid">Bid#: 20-0182</div>
  <div class="rule" style="top:229px"></div>

  <table class="line-items">
    <thead>
      <tr><th style="width:196px">Item</th><th class="num">Quantity</th><th class="num">U/M</th><th class="money">Unit<br>$</th><th class="money">Total $</th></tr>
    </thead>
    <tbody>
      <tr><td>Form, Pour &amp; Finish New Concrete Slab (24' x 24' x 4"). Includes: 3000psi Concrete Mix, Footer (12" x 8") with One (#5) Continuous Rebar, Wire Mesh Reinforcement and Saw-Cut Expansion Joints</td><td class="num">576</td><td class="num">SF</td><td class="money">$8.65</td><td class="money strong">$4,982.40</td></tr>
      <tr><td>OPTIONAL: Add (2' x 24' x 4") Small Ramp Area</td><td class="num">48</td><td class="num">SF</td><td class="money">$8.65</td><td class="money strong">$415.20</td></tr>
      <tr class="total"><td></td><td></td><td colspan="2" class="money strong">Total Price</td><td class="money strong">$5,397.60</td></tr>
    </tbody>
  </table>
</section>

<section class="page page--terms">
  <svg class="page-frame" width="377" height="533" viewBox="0 0 377 533" aria-hidden="true">
    <polygon points="16,0 37,0 37,283 16,295" fill="var(--brand-red)"/>
    <polygon points="16,295 37,283 37,507 377,507 377,526 16,526" fill="var(--brand-dark)"/>
    <polygon points="36,390 50,398 50,487 36,495 22,487 22,398" fill="var(--brand-red)" stroke="var(--paper)" stroke-width="1.2"/>
    <line x1="24" y1="428" x2="50" y2="428" stroke="var(--brand-dark)" stroke-width=".8"/>
    <line x1="24" y1="457" x2="50" y2="457" stroke="var(--brand-dark)" stroke-width=".8"/>
    <g>
      <circle cx="37" cy="414" r="5" fill="var(--brand-dark)"/>
      <path d="M34.6 411.6c.4-.4.9-.3 1.1.1l.6 1c.2.4 0 .7-.3.9.4.8 1 1.4 1.8 1.8.2-.3.5-.5.9-.3l1 .6c.4.2.5.7.1 1.1-.6.6-1.500.7-2.300.2-1.4-.8-2.500-1.900-3.200-3.300-.4-.7-.3-1.500.3-2.100z" fill="#fff"/>
      <circle cx="37" cy="444" r="5" fill="var(--brand-dark)"/>
      <path d="M37 440.8a2.3 2.3 0 0 0-2.3 2.3c0 1.7 2.3 4 2.3 4s2.3-2.3 2.3-4a2.3 2.3 0 0 0-2.3-2.3z" fill="#fff"/>
      <circle cx="37" cy="443.1" r=".8" fill="var(--brand-dark)"/>
      <circle cx="37" cy="473" r="5" fill="var(--brand-dark)"/>
      <circle cx="37" cy="473" r="2.8" fill="none" stroke="#fff" stroke-width=".8"/>
      <path d="M34.2 473h5.6M37 470.2c1.2 1.4 1.2 4.2 0 5.6M37 470.2c-1.2 1.4-1.2 4.2 0 5.6" stroke="#fff" stroke-width=".6" fill="none"/>
    </g>
  </svg>
  <div class="brand-name">GRANITE LANE</div>

  <div class="terms-box">
    <div class="terms-title">Terms and Conditions</div>
    <ul class="terms-list">
      <li>Prices as quoted in this estimate are valid for (60) days only.</li>
      <li>Payment in full, less any previously paid amounts, is due to the Contractor upon completion of the proposed scope of work.</li>
      <li>All change order requests must be communicated in writing to the Contractor by the Client or their authorized representative.</li>
      <li>All measurements listed in this estimate are approximate and may vary slightly due to actual field conditions.</li>
      <li>It is agreed by the Contractor and the Client that complications and costs arising from unforeseen conditions and handling of unsuitable materials are not included in this estimate.</li>
      <li>Unless specifically listed in this estimate, the following items and their costs are not included: Maintenance of Traffic, Concrete Material Pumping, Testing, Excavation, Grading and Fill Material, Permits and Fees, Surveying and As-builts, Irrigation Repair, Landscaping and Root Mitigation, De-watering, Private Locates and Accessibility.</li>
      <li>Private utility locating services using radio detection devices and, when necessary, ground penetrating radar are offered by Granite Lane to assist in finding private utilities that may not have been located by the public one call system. Granite Lane will not be responsible for private utilities that have not been located nor for the failure of the above equipment to accurately detect existing utilities since the equipment is fallible and existing site conditions may preclude the ability of the equipment to detect an identifiable signal.</li>
    </ul>
  </div>

  <div class="signature" style="top:339px">Client Signature</div>
  <div class="signature" style="top:368px;width:85px">Date</div>

  <div class="contact" style="top:405px">+123 456 789 000<br>+123 456 789 000</div>
  <div class="contact-rule" style="top:428px"></div>
  <div class="contact" style="top:434px">00/0 Street Name City Area<br>Avenue, State Code-0000</div>
  <div class="contact-rule" style="top:457px"></div>
  <div class="contact" style="top:463px">your website link goes here<br>your email name goes here</div>
</section>

</body>
</html>
```